43 Year Old Construction firm needs Updated Business Card & Stationery Design

We are an established and well known (in our market) commercial construction firm. We need a cleaner and more modern look for our corporate identity material. We would like to continue to use our current colors and logo.
We are thinking about incorporating a slogan on our business card (either front or back): "Building lasting trust with every project we deliver." The text could change at some point. Our website is www.kradworth.example . Sample card is attached. Some will have more phone numbers, etc...
Updates

Target Market(s)

Commercial and institutional clients.

Industry/Entity Type

Construction Company

Contact Information for Business Card

See attached for existing card. But don't be constrained.

Requirements
Must have
• Logo, name, title, address, website, email, phone numbers (as few as one, as many as three)
• Slogan on front or back "Building lasting trust with every project we deliver"
• Use existing logo and colors

```html
<!DOCTYPE html>
<html lang="en">
<head>
<meta charset="utf-8">
<title>Kradworth Constructors – Business Card</title>
<link rel="stylesheet" href="https://fonts.googleapis.com/css2?family=Montserrat:wght@500;600;700&family=Source+Sans+3:wght@400;600&display=swap">
<style>
  :root {
    --canvas: #000000;
    --paper: #f4f4f4;
    --brand-blue: #0e4a8a;
    --brand-green: #0f9a4e;
    --wine: #8e3a4d;
    --wine-light: #a65566;
    --plum: #55344f;
    --plum-light: #6f4d68;
    --navy: #2e3050;
    --navy-light: #474a6c;
    --coral: #e8484a;
    --coral-light: #f06a6b;
    --white: #ffffff;
  }
  * { margin: 0; padding: 0; box-sizing: border-box; }
  html, body {
    width: 1200px; height: 1200px; overflow: hidden;
    background: var(--canvas);
  }
  .card {
    position: absolute;
    left: 213px;
    width: 777px;
    display: block;
  }
  .card--front { top: 112px; height: 431px; }
  .card--back  { top: 655px; height: 432px; }

  .paper { fill: var(--paper); }
  .chevron-blue { fill: var(--brand-blue); }
  .chevron-green { fill: var(--brand-green); }

  .band--address { fill: var(--wine); }
  .facet--address { fill: var(--wine-light); }
  .band--email { fill: var(--plum); }
  .facet--email { fill: var(--plum-light); }
  .band--phone { fill: var(--navy); }
  .facet--phone { fill: var(--navy-light); }
  .band--web { fill: var(--coral); }
  .facet--web { fill: var(--coral-light); }

  .icon-fill { fill: var(--white); }
  .icon-line { fill: none; stroke: var(--white); stroke-width: 2.2; stroke-linecap: round; stroke-linejoin: round; }

  .holder-name {
    font-family: "Montserrat", sans-serif;
    font-weight: 700;
    font-size: 20px;
    fill: var(--coral);
  }
  .contact-text {
    font-family: "Montserrat", sans-serif;
    font-weight: 500;
    font-size: 11px;
    fill: var(--white);
  }
  .company-name {
    font-family: "Montserrat", sans-serif;
    font-weight: 700;
    font-size: 25px;
    letter-spacing: 0.5px;
    fill: var(--brand-blue);
  }
  .slogan {
    font-family: "Source Sans 3", sans-serif;
    font-weight: 400;
    font-size: 17px;
    fill: var(--brand-blue);
  }
  .footer-bar--web { fill: var(--coral); }
  .footer-bar--phone { fill: var(--navy); }
  .footer-bar--email { fill: var(--plum); }
  .footer-text {
    font-family: "Montserrat", sans-serif;
    font-weight: 500;
    font-size: 9.5px;
    fill: var(--white);
  }
</style>
</head>
<body>

<!-- Front of card -->
<svg class="card card--front" viewBox="0 0 518 287" xmlns="http://www.w3.org/2000/svg" aria-label="Business card front">
  <rect class="paper" width="518" height="287"/>

  <!-- brand chevron -->
  <polygon class="chevron-green" points="38,0 56,0 200,142 56,287 38,287"/>
  <polygon class="chevron-blue" points="0,0 42,0 190,142 42,287 0,287"/>

  <text class="holder-name" x="88" y="126" text-anchor="middle">Martin R.</text>
  <text class="holder-name" x="88" y="154" text-anchor="middle">Delacroix</text>

  <!-- address row -->
  <g class="row row--address">
    <rect class="band--address" x="154" y="17" width="364" height="36"/>
    <polygon class="facet--address" points="154,17 230,17 266,53 154,53"/>
    <polygon class="band--address" points="154,19 188,53 154,87 120,53"/>
    <path class="icon-fill" d="M154 40 c-7 0 -11 5 -11 11 c0 8 11 19 11 19 s11 -11 11 -19 c0 -6 -4 -11 -11 -11z M154 47 a4 4 0 1 1 0 8 a4 4 0 1 1 0 -8z" fill-rule="evenodd"/>
    <text class="contact-text" x="240" y="31">2418 Harlow Street</text>
    <text class="contact-text" x="240" y="46">Fenwick, MO 63001-4410</text>
  </g>

  <!-- email row -->
  <g class="row row--email">
    <rect class="band--email" x="198" y="62" width="320" height="35"/>
    <polygon class="facet--email" points="198,62 274,62 309,97 198,97"/>
    <polygon class="band--email" points="198,63 232,97 198,131 164,97"/>
    <rect class="icon-line" x="186" y="89" width="24" height="17"/>
    <polyline class="icon-line" points="186,89 198,99 210,89"/>
    <text class="contact-text" x="288" y="82">martind@kradworth.example</text>
  </g>

  <!-- phone row -->
  <g class="row row--phone">
    <rect class="band--phone" x="198" y="190" width="320" height="35"/>
    <polygon class="facet--phone" points="198,190 240,190 275,225 198,225"/>
    <polygon class="band--phone" points="198,156 232,190 198,224 164,190"/>
    <path class="icon-fill" d="M190 178 l5 -2 l4 8 l-3 3 c1 3 4 6 7 7 l3 -3 l8 4 l-2 5 c-10 1 -23 -12 -22 -22z"/>
    <text class="contact-text" x="286" y="211">555 014 2290</text>
  </g>

  <!-- web row -->
  <g class="row row--web">
    <rect class="band--web" x="154" y="234" width="364" height="36"/>
    <polygon class="facet--web" points="154,234 190,234 226,270 154,270"/>
    <polygon class="band--web" points="154,200 188,234 154,268 120,234"/>
    <path class="icon-line" d="M142 227 a17 17 0 0 1 24 0"/>
    <path class="icon-line" d="M146 232 a11 11 0 0 1 16 0"/>
    <path class="icon-line" d="M150 237 a5 5 0 0 1 8 0"/>
    <circle class="icon-fill" cx="154" cy="242" r="2.2"/>
    <text class="contact-text" x="240" y="256">www.kradworth.example</text>
  </g>
</svg>

<!-- Back of card -->
<svg class="card card--back" viewBox="0 0 518 288" xmlns="http://www.w3.org/2000/svg" aria-label="Business card back">
  <rect class="paper" width="518" height="288"/>

  <text class="company-name" x="259" y="106" text-anchor="middle">KRADWORTH CONSTRUCTORS</text>

  <text class="slogan" x="259" y="190" text-anchor="middle">“ Building lasting trust with every project we deliver ”</text>

  <g class="footer">
    <rect class="footer-bar--web" x="0" y="229" width="173" height="26"/>
    <rect class="footer-bar--phone" x="173" y="229" width="172" height="26"/>
    <rect class="footer-bar--email" x="345" y="229" width="173" height="26"/>
    <text class="footer-text" x="86.5" y="245.5" text-anchor="middle">www.kradworth.example</text>
    <text class="footer-text" x="259" y="245.5" text-anchor="middle">555 014 7731</text>
    <text class="footer-text" x="431.5" y="245.5" text-anchor="middle">martind@kradworth.example</text>
  </g>
</svg>

</body>
</html>
```